Retail brand for customisable denim jackets

Need an interactive website where people can select sizing and colour, as well as a customisable option to add selected patches and/or pins from the inventory to be able to be drag and dropped on various locations on the denim jacket.
Base jackets also available to be bought.

Include online payment options with security.
Contact us button / feedback button

Target Market(s)

Teenagers and young adults but could include adults or others.
Currently not targeted at children.

Industry/Entity Type

Clothing Brand

Coding

Coded - Design and coding required

Number of Pages Required

3 page

Requirements
Must have
• Drag and drop of patches and pins from inventory.

A panel laying out how to order Eg 1) Pick your jacket 2) Choose your patches and pins. 3) Check out your master creation!

Colours: Light Blue, Dark Blue, Black
2d model style with the different faces of the jacket, Eg front view, back view, sleeves, shoulders etc. (for patch and pin placement)
Nice to have
• 3d cgi model of denim jacket for customer to see what their product would look like.

```html
<!DOCTYPE html>
<html lang="en">
<head>
<meta charset="utf-8">
<title>Bluecraft Denim</title>
<link href="https://fonts.googleapis.com/css2?family=Montserrat:wght@400;500;600;700&family=Playfair+Display:ital,wght@0,500;0,700;1,700&display=swap" rel="stylesheet">
<style>
:root{
  --blue:#2e6fd6;
  --blue-dark:#1f4f9c;
  --navy:#1e2f52;
  --ink:#222;
  --grey:#8a8a8a;
  --line:#d6dbe3;
  --footer:#1b1c1e;
  --footer-deep:#121315;
}
*{box-sizing:border-box;margin:0;padding:0}
html,body{width:1200px;height:3521px;overflow:hidden}
body{position:relative;font-family:'Montserrat',sans-serif;color:var(--ink);background:#fff}
.abs{position:absolute}
a{color:inherit;text-decoration:none}

/* top bar */
.topbar{left:0;top:0;width:1200px;height:34px;background:var(--blue-dark);color:#fff;font-size:13px}
.topbar .welcome{left:60px;top:9px}
.topbar .links{left:444px;top:9px;display:flex;gap:30px}
.topbar .sign{right:60px;top:9px;display:flex;gap:8px;align-items:center}

/* nav */
.nav{left:0;top:34px;width:1200px;height:90px;background:#fff}
.brand{left:62px;top:32px;display:flex;align-items:center;gap:10px;font-weight:700;font-size:17px;color:var(--navy)}
.brand .dot{width:22px;height:22px;border-radius:50%;background:var(--navy)}
.menu{left:292px;top:0;height:90px;display:flex;font-weight:700;font-size:14px}
.menu a{display:flex;align-items:center;padding:0 19px;height:90px;border-bottom:5px solid transparent}
.menu a.active{color:var(--blue);border-bottom-color:var(--blue)}
.nav .search{left:992px;top:34px}
.nav .cart{left:1042px;top:34px;display:flex;gap:8px;font-weight:700;font-size:14px;align-items:center}

/* hero */
.hero{left:0;top:124px;width:1200px;height:577px}
.panel{position:absolute;top:0;height:577px}
.p1{left:0;width:399px;background:linear-gradient(160deg,#8c7b66,#3d5f9c 55%,#23303f)}
.p2{left:399px;width:451px;background:linear-gradient(180deg,#c9ccce,#9aa2aa 60%,#5b6470)}
.p3{left:850px;width:350px;background:linear-gradient(170deg,#1f2a38,#28507f 50%,#11171f)}
.sale{left:495px;top:133px;width:227px;height:225px;background:rgba(30,47,82,.88);border:2px solid #fff;outline:1px solid rgba(255,255,255,.6);outline-offset:-8px;color:#fff;text-align:center}
.sale .k{margin-top:28px;font-size:16px;font-weight:500}
.sale .big{font-size:48px;font-weight:600;margin-top:6px;letter-spacing:1px}
.sale .up{font-size:16px;margin-top:2px;display:flex;align-items:center;justify-content:center;gap:10px}
.sale .up:before,.sale .up:after{content:"";width:28px;height:1px;background:#fff}
.sale .off{font-size:26px;font-weight:600;margin-top:8px}
.shop{left:522px;top:408px;width:157px;height:43px;background:var(--blue);color:#fff;font-weight:700;font-size:17px;display:flex;align-items:center;justify-content:center}
.dots{left:558px;top:530px;display:flex;gap:10px}
.dots i{width:12px;height:12px;background:#fff;transform:rotate(45deg);display:block}
.dots i:first-child{background:var(--blue)}

/* ordering steps */
.step{top:735px;height:84px;color:#fff;display:flex;align-items:center;gap:16px}
.s1{left:62px;width:360px;background:var(--blue-dark);clip-path:polygon(0 0,92% 0,100% 50%,92% 100%,0 100%);padding-left:26px}
.s2{left:410px;width:385px;background:#76797d;clip-path:polygon(0 0,92% 0,100% 50%,92% 100%,0 100%,8% 50%);padding-left:55px}
.s3{left:775px;width:362px;background:var(--blue-dark);clip-path:polygon(0 0,100% 0,100% 100%,0 100%,8% 50%);padding-left:58px}
.step b{display:block;font-size:19px;font-weight:700;white-space:nowrap}
.step small{font-size:14px}

/* section titles */
.title{left:62px;width:1075px;height:40px;display:flex;align-items:center;justify-content:center}
.title:before{content:"";position:absolute;left:0;right:0;top:50%;height:1px;background:var(--line)}
.title span{position:relative;background:#fff;padding:0 42px;font-family:'Playfair Display',serif;font-weight:500;font-size:35px}
.title i{position:absolute;z-index:2;top:14px;width:12px;height:12px;background:var(--blue);transform:rotate(45deg)}

/* handpicked tiles */
.tile{position:absolute;color:#fff}
.tile .frame{position:absolute;inset:20px;border:2px solid #fff}
.tile .t1{position:absolute;font-family:'Playfair Display',serif;font-style:italic;font-weight:700;font-size:30px}
.tile .t2{position:absolute;font-weight:700;font-size:30px;white-space:nowrap}
.tile .btn{position:absolute;background:var(--blue);font-weight:700;font-size:17px;padding:12px 14px;border:2px solid #fff}

/* products */
.products{left:57px;top:1814px;width:1077px;height:790px;border:1px solid #e4e7ec}
.card{position:absolute;width:250px;text-align:center}
.card .img{height:288px;border:1px solid #e2e5ea;position:relative}
.card .tag{position:absolute;left:14px;top:14px;width:50px;height:50px;border-radius:50%;background:var(--blue);color:#fff;font-weight:700;font-size:18px;display:flex;align-items:center;justify-content:center}
.card h4{font-size:15px;font-weight:600;margin-top:18px}
.card p{font-size:27px;color:var(--blue);margin-top:10px}

/* testimonial */
.avatar{left:541px;top:2758px;width:117px;height:117px;border-radius:50%;background:linear-gradient(160deg,#e9edf3,#3f6fb4)}
.arrow{top:2800px}
.person{left:0;width:1200px;text-align:center}
.quote{left:280px;top:2966px;width:640px;text-align:center;font-size:15px;line-height:26px}

/* footer */
.footer{left:0;top:3092px;width:1200px;height:429px;background:var(--footer);color:#fff}
.fcol{position:absolute;top:58px}
.fcol h5{font-size:13px;font-weight:700;margin-bottom:32px}
.fcol a{display:block;font-size:14px;color:#c6c8cc;margin-bottom:8px;line-height:17px}
.socials{left:722px;top:105px;display:flex;gap:16px}
.socials i{width:42px;height:42px;border-radius:50%;background:#fff;display:block}
.subhead{left:720px;top:182px;font-size:13px;font-weight:700}
.subhead em{font-family:'Playfair Display',serif;font-style:italic;margin:0 4px}
.email{left:723px;top:222px;width:283px;height:40px;border:1px solid #4a4c50;font-size:14px;color:#c6c8cc;padding:11px 18px}
.subbtn{left:1006px;top:222px;width:131px;height:40px;background:var(--blue);font-weight:700;font-size:14px;display:flex;align-items:center;justify-content:center}
.totop{left:1102px;top:314px;width:32px;height:32px;background:var(--blue);display:flex;align-items:center;justify-content:center}
.bottom{left:0;top:375px;width:1200px;height:54px;background:var(--footer-deep);border-top:1px solid #2e3034;text-align:center;font-size:12px;color:#c6c8cc;padding-top:28px}
.bottom:before{content:"";position:absolute;left:592px;top:-1px;border:8px solid transparent;border-top-color:var(--blue)}
</style>
</head>
<body>

<div class="abs topbar">
  <span class="abs welcome">Welcome to Bluecraft Denim Store!</span>
  <div class="abs links"><a>COVID-19</a><a>Feedback</a><a>Track Order</a><a>Find Stores &amp; Services</a><a>Help</a></div>
  <div class="abs sign"><svg width="18" height="18" viewBox="0 0 18 18"><circle cx="9" cy="9" r="8" fill="none" stroke="#fff" stroke-width="1.5"/><circle cx="9" cy="7" r="3" fill="#fff"/><path d="M3.5 14c1.5-3 9.5-3 11 0" fill="#fff"/></svg>Signin/Register</div>
</div>

<header class="abs nav">
  <div class="abs brand"><span class="dot"></span>Bluecraft Denim</div>
  <nav class="abs menu">
    <a class="active">MEN</a><a>WOMEN</a><a>PATCHES</a><a>NEW ARRIVALS</a><a>CUSTOMIZE</a><a>CONTACT US</a>
  </nav>
  <svg class="abs search" width="22" height="22" viewBox="0 0 22 22"><circle cx="9" cy="9" r="7" fill="none" stroke="#2e6fd6" stroke-width="3"/><path d="M14 14l6 6" stroke="#2e6fd6" stroke-width="3"/></svg>
  <div class="abs cart"><svg width="22" height="22" viewBox="0 0 22 22"><path d="M2 7h18l-1 13H3z" fill="#2e6fd6"/><path d="M7 8V5a4 4 0 0 1 8 0v3" fill="none" stroke="#2e6fd6" stroke-width="2"/></svg>CART: 2</div>
</header>

<section class="abs hero">
  <div class="panel p1" role="img" aria-label="Young woman in a light blue denim jacket smiling on a city street"></div>
  <div class="panel p2" role="img" aria-label="Woman in a denim jacket leaning against a metal mesh wall"></div>
  <div class="panel p3" role="img" aria-label="Woman in a denim jacket and striped dress under a neon sign"></div>
  <div class="abs sale">
    <div class="k">MID-SEASON</div>
    <div class="big">SALE</div>
    <div class="up">UP TO</div>
    <div class="off">50 <small style="font-size:16px">%</small>&nbsp; OFF</div>
  </div>
  <a class="abs shop">SHOP NOW</a>
  <div class="abs dots"><i></i><i></i><i></i><i></i></div>
</section>

<div class="abs step s1">
  <svg width="34" height="34" viewBox="0 0 34 34"><circle cx="17" cy="17" r="14" fill="none" stroke="#fff" stroke-width="3"/><text x="17" y="23" text-anchor="middle" font-family="Montserrat,sans-serif" font-weight="700" font-size="16" fill="#fff">1</text></svg>
  <div><b>PICK YOUR JACKET</b><small>Choose size &amp; colour</small></div>
</div>
<div class="abs step s2">
  <svg width="34" height="34" viewBox="0 0 34 34"><circle cx="17" cy="17" r="14" fill="none" stroke="#fff" stroke-width="3"/><text x="17" y="23" text-anchor="middle" font-family="Montserrat,sans-serif" font-weight="700" font-size="16" fill="#fff">2</text></svg>
  <div><b>ADD PATCHES &amp; PINS</b><small>Drag &amp; drop onto any view</small></div>
</div>
<div class="abs step s3">
  <svg width="34" height="34" viewBox="0 0 34 34"><circle cx="17" cy="17" r="14" fill="none" stroke="#fff" stroke-width="3"/><text x="17" y="23" text-anchor="middle" font-family="Montserrat,sans-serif" font-weight="700" font-size="16" fill="#fff">3</text></svg>
  <div><b>CHECK OUT</b><small>Secure online payment</small></div>
</div>

<div class="abs title" style="top:877px"><i style="left:378px"></i><span>HandPicked</span><i style="left:686px"></i></div>

<div class="tile" style="left:59px;top:972px;width:333px;height:333px;background:linear-gradient(150deg,#2f6d86,#3a5d78 50%,#c57a3b)" role="img" aria-label="Close-up of enamel pins on a denim jacket">
  <div class="frame"></div>
  <div class="t1" style="left:38px;top:30px">30%</div>
  <div class="t2" style="left:38px;top:72px;font-size:26px">OFFERS</div>
  <a class="btn" style="left:38px;top:128px">SHOP NOW</a>
</div>
<div class="tile" style="left:409px;top:972px;width:382px;height:682px;background:linear-gradient(180deg,#a9b2b6,#7b8a96 55%,#4e6477)" role="img" aria-label="Woman with glasses in a denim jacket sitting against a wall">
  <div class="frame" style="inset:17px"></div>
  <div class="t1" style="left:102px;top:28px">Winter</div>
  <div class="t2" style="left:102px;top:74px">COLLECTIONS</div>
</div>
<div class="tile" style="left:805px;top:972px;width:332px;height:333px;background:linear-gradient(160deg,#6f7e88,#5d7892 60%,#8aa4bd)" role="img" aria-label="Man in a cap and denim jacket seen from behind">
  <div class="frame" style="inset:20px 20px 24px 14px"></div>
  <div class="t1" style="left:35px;top:40px;font-size:26px">Mens</div>
  <div class="t2" style="left:35px;top:78px;font-size:26px">COLLECTIONS</div>
</div>
<div class="tile" style="left:59px;top:1319px;width:333px;height:332px;background:linear-gradient(150deg,#b49a78,#5e7694 55%,#3b4d66)" role="img" aria-label="Assorted embroidered patches and enamel pins on denim">
  <div class="frame"></div>
  <div class="t1" style="left:110px;top:38px;font-size:26px">Patches &amp;</div>
  <div class="t2" style="left:110px;top:76px;font-size:32px">PINS</div>
</div>
<div class="tile" style="left:805px;top:1319px;width:332px;height:332px;background:linear-gradient(160deg,#c8cdd0,#7a6a5e 55%,#3c4652)" role="img" aria-label="Bearded man in a customised jacket sitting by a window">
  <div class="frame" style="inset:20px 18px 24px 16px"></div>
  <div class="t1" style="left:38px;top:210px;font-size:26px">Design</div>
  <div class="t2" style="left:38px;top:248px;font-size:32px">YOUR OWN</div>
</div>

<div class="abs title" style="top:1710px"><i style="left:378px"></i><span>Top collections</span><i style="left:686px"></i></div>

<section class="abs products">
  <div class="card" style="left:14px;top:15px"><div class="img" style="background:#5f95e3" role="img" aria-label="Blue denim jacket laid flat"><span class="tag">20<small style="font-size:9px">%</small></span></div><h4>Denim Jacket 1 Dress</h4><p>$ 61.19</p></div>
  <div class="card" style="left:282px;top:15px"><div class="img" style="background:linear-gradient(160deg,#37b8d3,#2c5f9c 60%,#1f2c44)" role="img" aria-label="Man in a denim shirt crouching against a turquoise wall"></div><h4>Denim Jacket 2 Dress</h4><p>$ 112.50</p></div>
  <div class="card" style="left:546px;top:15px"><div class="img" style="background:linear-gradient(160deg,#ececec,#9bb3cf 60%,#d8d8d8)" role="img" aria-label="Woman in a denim shirt working on a laptop"></div><h4>Denim Jacket 3 Dress</h4><p>$ 96.00</p></div>
  <div class="card" style="left:811px;top:15px"><div class="img" style="background:linear-gradient(150deg,#9fb6cf,#6f8fb3 55%,#4a3a32)" role="img" aria-label="Light denim jacket with sunglasses on a wooden floor"><span class="tag">40<small style="font-size:9px">%</small></span></div><h4>Denim Jacket 4 Dress</h4><p>$ 121.19</p></div>

  <div class="card" style="left:14px;top:410px"><div class="img" style="background:linear-gradient(160deg,#f0f0f0,#a9bcd3 60%,#e8e8e8)" role="img" aria-label="Blonde woman in a denim jacket using a phone"><span class="tag">20<small style="font-size:9px">%</small></span></div><h4>Denim Jacket 1 Dress</h4><p>$ 61.19</p></div>
  <div class="card" style="left:282px;top:410px"><div class="img" style="background:linear-gradient(160deg,#f6ad3a,#f5a623 50%,#2c3a55)" role="img" aria-label="Woman in a dark denim jacket against an orange wall"></div><h4>Denim Jacket 2 Dress</h4><p>$ 112.50</p></div>
  <div class="card" style="left:546px;top:410px"><div class="img" style="background:linear-gradient(160deg,#dfe2e6,#6b8cbf 60%,#d9dce0)" role="img" aria-label="Young woman in a denim jacket smiling"></div><h4>Denim Jacket 3 Dress</h4><p>$ 96.00</p></div>
  <div class="card" style="left:811px;top:410px"><div class="img" style="background:linear-gradient(160deg,#d8dadc,#4a5d78 55%,#2a2a2e)" role="img" aria-label="Woman in a denim jacket and black t-shirt"><span class="tag">40<small style="font-size:9px">%</small></span></div><h4>Denim Jacket 4 Dress</h4><p>$ 121.19</p></div>
</section>

<div class="abs title" style="top:2672px"><i style="left:378px"></i><span>Customer Says</span><i style="left:686px"></i></div>

<svg class="abs arrow" style="left:462px" width="20" height="32" viewBox="0 0 20 32"><path d="M16 3L4 16l12 13" fill="none" stroke="#9a9a9a" stroke-width="4"/></svg>
<div class="abs avatar" role="img" aria-label="Portrait of a smiling customer"></div>
<svg class="abs arrow" style="left:720px" width="20" height="32" viewBox="0 0 20 32"><path d="M4 3l12 13L4 29" fill="none" stroke="#9a9a9a" stroke-width="4"/></svg>
<div class="abs person" style="top:2890px;font-family:'Playfair Display',serif;font-style:italic;font-weight:700;font-size:24px">Mara Lind</div>
<div class="abs person" style="top:2926px;font-size:15px;color:var(--grey)">Fashion Designer</div>
<p class="abs quote">These guys are really professional, helpful and friendly.&nbsp; They offer help as a team which is well coordinated, at a competitive rate. Early days yet, but really pleased with the work they have done.</p>

<footer class="abs footer">
  <div class="fcol" style="left:68px"><h5>SHOPS</h5><a>New In</a><a>Women</a><a>Men</a><a>Patches &amp; Pins</a><a>Sale &amp; Special Offers</a><a>Rating</a></div>
  <div class="fcol" style="left:267px"><h5>INFORMATION</h5><a>About us</a><a>Customer Service</a><a>New Collection</a><a>Best Sellers</a><a>Privacy policy</a><a>Terms &amp; condition</a></div>
  <div class="fcol" style="left:474px"><h5>CUSTOMER SERVICE</h5><a style="margin-top:4px">Orders and Returns</a><a>Contact Us</a><a>Help &amp; FAQs</a><a>Store Locations</a></div>
  <div class="fcol" style="left:720px"><h5>STAY CONNECTED</h5></div>
  <div class="abs socials"><i></i><i></i><i></i><i></i></div>
  <div class="abs subhead">SUBSCRIBE<em>in</em>OUR NEWS LETTER</div>
  <div class="abs email">Enter Your Email Address</div>
  <div class="abs subbtn">SUBSCRIBE</div>
  <div class="abs totop"><svg width="16" height="10" viewBox="0 0 16 10"><path d="M2 8l6-6 6 6" fill="none" stroke="#fff" stroke-width="2"/></svg></div>
  <div class="abs bottom">Bluecraft Denim© 2020. All Rights Reserved.</div>
</footer>

</body>
</html>
```